Natural Cosmetics need a Packaging Design

We need a PACKAGING design for labels on hand/body wash bottles and soap paper boxes.
We target at high end markets.
We expect a contemporary and trendy design.
We don't need a separate logo. The brand name "Va Mirel" acts as the logo.
We want a modern and classic font for "Va Mirel".
Please see attached pictures for packaging samples.

Industry/Entity Type

Cosmetics

Requirements
Should not have
• a separate logo from the brand name

```html
<!DOCTYPE html>
<html lang="en">
<head>
<meta charset="utf-8">
<title>Va Mirel – Packaging Labels</title>
<link rel="stylesheet" href="https://fonts.googleapis.com/css2?family=Cabin:wght@400;500&display=swap">
<style>
  :root {
    --backdrop: #f2f1ef;
    --label-white: #ffffff;
    --ink: #111111;
    --text-dark: #2a2a2a;
    --gold-light: #f3dc9a;
    --gold-mid: #c9a24a;
    --gold-dark: #7a5a1c;
    --silver-light: #f4f4f4;
    --silver-mid: #a9adb2;
    --silver-dark: #55595e;
    --label-edge: #dddcd8;
  }
  * { margin: 0; padding: 0; box-sizing: border-box; }
  html, body { width: 1172px; height: 1200px; overflow: hidden; }
  body {
    position: relative;
    background: var(--backdrop);
    font-family: "Cabin", sans-serif;
    color: var(--text-dark);
  }
  .label {
    position: absolute;
    background: var(--label-white);
    border: 1px solid var(--label-edge);
  }
  .brand-name {
    position: absolute;
    left: 50%;
    transform: translateX(-50%);
    background: var(--ink);
    color: var(--label-white);
    display: flex;
    align-items: center;
    justify-content: center;
    font-weight: 400;
    white-space: nowrap;
  }
  .product-name {
    position: absolute;
    left: 0; right: 0;
    text-align: center;
    text-transform: uppercase;
    letter-spacing: 0.12em;
    font-weight: 400;
  }
  .accent-band { position: absolute; left: 0; right: 0; }
  .accent-band .shine { height: 3px; background: linear-gradient(90deg, var(--gold-dark), var(--gold-light) 30%, var(--gold-mid) 55%, var(--gold-light) 80%, var(--gold-dark)); }
  .accent-band.silver .shine { background: linear-gradient(90deg, var(--silver-dark), var(--silver-light) 30%, var(--silver-mid) 55%, var(--silver-light) 80%, var(--silver-dark)); }
  .accent-band .bar { background: var(--ink); margin-top: 3px; }
  .volume {
    position: absolute;
    left: 0; right: 0;
    text-align: center;
  }

  /* Body wash labels */
  .body-wash { top: 533px; width: 258px; height: 358px; }
  .body-wash.gold-edition { left: 105px; }
  .body-wash.silver-edition { left: 434px; }
  .body-wash .brand-name { top: 71px; width: 176px; height: 44px; font-size: 32px; }
  .body-wash .product-name { top: 191px; font-size: 23px; }
  .body-wash .accent-band { top: 279px; }
  .body-wash .accent-band .bar { height: 14px; }
  .body-wash .volume { top: 326px; font-size: 14px; }

  /* Soap wrap */
  .soap-wrap { left: 768px; top: 229px; width: 298px; height: 287px; }
  .soap-wrap .brand-name { top: 38px; width: 179px; height: 49px; font-size: 34px; }
  .soap-wrap .product-name { top: 115px; font-size: 22px; }
  .soap-wrap .accent-band { top: 179px; }
  .soap-wrap .accent-band .bar { height: 15px; }
  .soap-wrap .volume { top: 236px; font-size: 14px; }

  /* Hand wash label */
  .hand-wash { left: 815px; top: 914px; width: 205px; height: 150px; }
  .hand-wash .brand-name { top: 20px; width: 103px; height: 29px; font-size: 21px; }
  .hand-wash .product-name { top: 61px; font-size: 15px; letter-spacing: 0.08em; }
  .hand-wash .accent-band { top: 93px; }
  .hand-wash .accent-band .bar { height: 11px; }
  .hand-wash .volume { top: 126px; font-size: 10px; }
</style>
</head>
<body>

  <section class="label body-wash gold-edition">
    <div class="brand-name">Va Mirel</div>
    <div class="product-name">Body Wash</div>
    <div class="accent-band"><div class="shine"></div><div class="bar"></div></div>
    <div class="volume">250ml</div>
  </section>

  <section class="label body-wash silver-edition">
    <div class="brand-name">Va Mirel</div>
    <div class="product-name">Body Wash</div>
    <div class="accent-band silver"><div class="shine"></div><div class="bar"></div></div>
    <div class="volume">250ml</div>
  </section>

  <section class="label soap-wrap">
    <div class="brand-name">Va Mirel</div>
    <div class="product-name">Beauty Soap</div>
    <div class="accent-band"><div class="shine"></div><div class="bar"></div></div>
    <div class="volume">100g</div>
  </section>

  <section class="label hand-wash">
    <div class="brand-name">Va Mirel</div>
    <div class="product-name">Hand Wash</div>
    <div class="accent-band"><div class="shine"></div><div class="bar"></div></div>
    <div class="volume">100ml</div>
  </section>

</body>
</html>
```